Spiritual Healing bussiness needs logo/business card

Simple, clean looking logo/card
For spiritual business with healing services and occult rituals

Contact Information for Business Card

Needs my name: Corwin Halley
Business name: Veyra Healing Shop
Services provided and worded in this way:

Reiki Healing
Tarot
Oils
Rituals Of Change

Can look occult like but with light energy.

Colors
0255a3
3276b5
85abd2
33a6d7
85cae6
0292cd

```html
<!DOCTYPE html>
<html lang="en">
<head>
<meta charset="utf-8">
<title>Corwin Halley – Healing Card</title>
<link rel="stylesheet" href="https://fonts.googleapis.com/css2?family=Montserrat:wght@700&family=Quicksand:wght@400&display=swap">
<style>
  :root {
    --card-blue: #4273b8;
    --leaf-green: #78c49c;
    --text-white: #ffffff;
  }
  html, body {
    margin: 0;
    padding: 0;
    width: 1200px;
    height: 1200px;
    overflow: hidden;
    background: var(--card-blue);
  }
  .card {
    display: block;
    width: 1200px;
    height: 1200px;
  }
  .card-background { fill: var(--card-blue); }
  .brand-dot { fill: var(--leaf-green); }
  .brand-name {
    font-family: "Quicksand", sans-serif;
    font-weight: 400;
    font-size: 58px;
    fill: var(--leaf-green);
  }
  .owner-name {
    font-family: "Montserrat", sans-serif;
    font-weight: 700;
    font-size: 146px;
    fill: var(--leaf-green);
  }
  .service-line {
    font-family: "Quicksand", sans-serif;
    font-weight: 400;
    font-size: 88px;
    fill: var(--text-white);
  }
</style>
</head>
<body>
  <svg class="card" viewBox="0 0 1200 1200" xmlns="http://www.w3.org/2000/svg" aria-label="Corwin Halley business card">
    <rect class="card-background" x="0" y="0" width="1200" height="1200"/>

    <g class="brand-block">
      <circle class="brand-dot" cx="985" cy="250" r="150"/>
      <text class="brand-name" x="1135" y="520" text-anchor="end">Veyra Healing Shop</text>
    </g>

    <text class="owner-name" transform="translate(175 1130) rotate(-90)"
          textLength="1065" lengthAdjust="spacingAndGlyphs">CORWIN HALLEY</text>

    <g class="services" text-anchor="end">
      <text class="service-line" x="1134" y="871" textLength="524" lengthAdjust="spacingAndGlyphs">Reiki Healing</text>
      <text class="service-line" x="1134" y="978" textLength="473" lengthAdjust="spacingAndGlyphs">Tarot - Oils</text>
      <text class="service-line" x="1134" y="1089" textLength="770" lengthAdjust="spacingAndGlyphs">Rituals Of Change</text>
    </g>
  </svg>
</body>
</html>
```